Mobile App Flyer for Takeaway Tiplo

We need a single A4 page flyer to promote our mobile apps for takeaway food solution.

Please visit our web site www.tiplo-example.com and review the retail page for further details but here are a number of the benefits that I'd like to try to include in the flyer.

I do need a catchy title too...

TAKEAWAYS & RESTAURANTS
Tap into the growth market of mobile and online food ordering. With over 51% of UK online ecommerce sales now being conducted on mobiles devices* it’s crucial takeaways and restaurants adopt a suitable mobile strategy.
* Source: KVDO / Borvanta 2016
Stay independent. Go mobile with an online food ordering app that is dedicated and designed specifically for your business. Unlike other solutions, we don’t encourage your customer to use a shared app that then promotes your competitors’ businesses to your customers!
We don’t charge order commission, just a small fixed monthly fee, (pricing published on our web site). As you grow your mobile business you keep all the profits!
Benefit from better Zentrix search results. Did you know Zentrix now favours and ranks businesses with mobile apps higher than those without?
Differentiate your business against other local businesses, create a buzz around your business going “Mobile”!
Free-up your business phone line at peak periods, never miss another order.
Save staff time by accepting unlimited mobile and on-line orders simultaneously, no need to take a call and write the orders down, it also minimises mistakes.
If you buy our Business or Business Plus package we will also provide you an online shop that can be added to your website!
If you’re thinking this isn’t going to be cheap, check our pricing on our web site, you’re going to be very pleasantly surprised.
Attractive interactive menus, show-off your business and food to its best.
Convenience for your customers:
No more holding or busy signal when trying to place an order.
Customer’s order history is saved in the app making re-ordering fast and convenient.
Customers can use convenient online payment providers such as QUIDLY, as well as traditional credit cards or of course, cash-on-collection.
Easily and quickly update your menu with seasonal changes, menu items, pricing and even delivery options.
Send promotions to your customers and advise them of seasonal opening times, even message them each time they are close to your business!
Launch an in-app loyalty programme, which rewards your loyal customers and generates repeat business.
There are many reason you should be considering going mobile if. Please call us on 01632 960457 or email us at Info@Tiplo-example.com to discuss your requirements with us.

Target Market(s)

Owners of takeaways and restaurants

Font styles to use
Sans Serif

Colors
33b8a4
3176b5
faa54b

Requirements
Must have
• Tiplo white and blue logo from website
• Features doc has some screen shots that could be used.
• The format must be reusable for other products so if I develop an app for a golf course, for example, I could use the same layout but change the primary colour of the flyer.
• Doesn't have to be identical to web site but shouldn't be poles apart so that it looks odd!
Nice to have
• At least one picture of a smart phone.

```html
<!DOCTYPE html>
<html lang="en">
<head>
<meta charset="utf-8">
<title>Tiplo – Food Retail Solution</title>
<link rel="stylesheet" href="https://fonts.googleapis.com/css2?family=Open+Sans:wght@400;600;700&display=swap">
<style>
  :root {
    --primary: #2f74b5;
    --accent: #f7a24a;
    --text: #7a7a7a;
    --paper: #ffffff;
    --device: #eef0f2;
  }
  * { margin: 0; padding: 0; box-sizing: border-box; }
  html, body { width: 849px; height: 1200px; overflow: hidden; }
  body { background: var(--paper); font-family: "Open Sans", Arial, sans-serif; position: relative; }

  .masthead {
    position: absolute; left: 0; top: 0; width: 849px; height: 86px;
    background: var(--primary);
  }
  .masthead h1 {
    position: absolute; left: 34px; top: 26px;
    color: #fff; font-weight: 400; font-size: 27px; letter-spacing: 0.5px;
  }

  .phone {
    position: absolute; left: -40px; top: 152px; width: 180px; height: 690px;
    border-radius: 28px; background: var(--device);
    box-shadow: 0 0 0 2px #d8dbde;
  }
  .phone-screen {
    position: absolute; left: 12px; top: 88px; width: 156px; height: 520px;
    background: linear-gradient(160deg, #f8ad55, #f39a3f);
  }

  .column { position: absolute; width: 207px; }
  .column h2 {
    color: var(--accent); font-weight: 600; font-size: 20px; line-height: 24px; margin-bottom: 6px;
  }
  .column p {
    color: var(--text); font-size: 10.6px; line-height: 13px; overflow: hidden;
  }
  .col-left { left: 212px; top: 178px; }
  .col-left .intro { height: 352px; }
  .col-left-lower { left: 212px; top: 630px; }
  .col-left-lower p { height: 222px; }
  .col-right { left: 433px; top: 178px; }
  .col-right p { height: 382px; }

  .hero-art {
    position: absolute; left: 430px; top: 608px; width: 400px; height: 482px;
    background: radial-gradient(ellipse at 50% 45%, #e3eef6 0%, #f3f7fa 55%, #ffffff 80%);
  }

  .footer {
    position: absolute; left: 0; bottom: 0; width: 849px; height: 102px;
    background: var(--primary);
  }
  .footer-contact {
    position: absolute; left: 50px; top: 27px; width: 540px;
    color: #fff; font-size: 13.5px; line-height: 19px;
  }
  .brand {
    position: absolute; right: 36px; top: 34px;
    display: flex; align-items: center; gap: 10px;
    color: #fff; font-weight: 700; font-size: 34px; line-height: 1;
  }
  .brand-dot { width: 14px; height: 14px; border-radius: 50%; background: #fff; }
</style>
</head>
<body>
  <header class="masthead"><h1>FOOD RETAIL SOLUTION</h1></header>

  <div class="phone" role="img" aria-label="Smartphone showing the orange takeaway ordering app screen">
    <div class="phone-screen"></div>
  </div>

  <section class="column col-left">
    <h2>Lorem ipsum</h2>
    <p class="intro">Dolor sit amet, consectetur adipisicing elit, sed do eiusmod tempor incididunt ut labore et dolore magna aliqua. Ut enim ad minim veniam, quis nostrud exercitation ullamco laboris nisi ut aliquip ex ea commodo consequat. Duis aute irure dolor in reprehenderit in voluptate velit esse cillum dolore eu fugiat nulla pariatur. Excepteur sint occaecat cupidatat non proident, sunt in culpa qui officia deserunt mollit anim id est laborum. Sed ut perspiciatis unde omnis iste natus error sit voluptatem accusantium doloremque laudantium, totam rem aperiam, eaque ipsa quae ab illo inventore veritatis et quasi architecto beatae vitae dicta sunt explicabo. Nemo enim ipsam voluptatem quia voluptas sit aspernatur aut odit aut fugit, sed quia consequuntur magni dolores eos qui ratione voluptatem sequi nesciunt.</p>
  </section>

  <section class="column col-left-lower">
    <h2>Nemo enim ipsam</h2>
    <p>Nemo enim ipsam voluptatem quia voluptas sit aspernatur aut odit aut fugit, sed quia consequuntur magni dolores eos qui ratione voluptatem sequi nesciunt. Neque porro quisquam est, qui dolorem ipsum quia dolor sit amet, consectetur, adipisci velit, sed quia non numquam eius modi tempora incidunt ut labore et dolore magnam aliquam quaerat voluptatem. Ut enim ad minima veniam, quis nostrum exercitationem ullam corporis suscipit laboriosam.</p>
  </section>

  <section class="column col-right">
    <h2>Duis aute irure dolor</h2>
    <p>Duis aute irure dolor in reprehenderit in voluptate velit esse cillum dolore eu fugiat nulla pariatur. Excepteur sint occaecat cupidatat non proident, sunt in culpa qui officia deserunt mollit anim id est laborum. Sed ut perspiciatis unde omnis iste natus error sit voluptatem accusantium doloremque laudantium, totam rem aperiam, eaque ipsa quae ab illo inventore veritatis et quasi architecto beatae vitae dicta sunt explicabo. Nemo enim ipsam voluptatem quia voluptas sit aspernatur aut odit aut fugit, sed quia consequuntur magni dolores eos qui ratione voluptatem sequi nesciunt. Neque porro quisquam est, qui dolorem ipsum quia dolor sit amet, consectetur, adipisci velit, sed quia non numquam eius modi tempora incidunt ut labore et dolore magnam aliquam quaerat voluptatem. Ut enim ad minima veniam, quis nostrum exercitationem.</p>
  </section>

  <div class="hero-art" role="img" aria-label="Illustration of raised hands holding smartphones surrounded by connected social and shopping icons"></div>

  <footer class="footer">
    <p class="footer-contact">Please call us on 01632 960457 or email us at Info@Tiplo-example.com<br>to discuss your requirements with us.</p>
    <div class="brand"><span class="brand-dot"></span>Tiplo</div>
  </footer>
</body>
</html>
```